Velmoria sailing boat for love and romance seekers*

We will pay extra 200$ for the winning design! So, we have a sailing boat, Halvard 58 KT called Velmoria, which we’d like to give for charter in Turkey and maybe other countries. Need a dedicated web page, with gallery, calendar, videos, customer reviews, possibility to pay down payment, legal disclosures and in 3 languages (English, Russian and Turkish). Also, there should be info on toys and crew. We can also agree on a monthly fee for maintenance and updates. It’s really important to show the details, so that potential customers can see clearly that the boat is in perfect shape. If needed, we can even make a 3D of the interior, or any other materials that you might need. People should also have the possibility to see the sailing routes that they can chose and experience while cruising. Additionally, we can organize diving tours, surfing lessons, and any other activities.

Target Market(s)

Family with kids. Those people that are looking for more luxury than what’s usually offered with other boats. This is a middle segment between usual boats and super luxury boats. Also, it’s for those people that want romance, love and are looking for Unforgetable experiences with their family.

Coding

Coded - Design and coding required

Number of Pages Required

3 page

Font styles to use
Sans Serif

Requirements
Must have
• Boat has lots of options, and we have a tender boat with which one can waterski, pull ringos and other toys. It’s big enough to carry all guests at the same time and comfortable to reach safely any remote beach location. We have brand new snorkeling and diving equipment, new paddle and surfing boards, new zumflo, Fintrak and life jackets for all age groups. Also, we should have a page on crew, who they are and whom additionally they can chose (for example cook or cleaning staff).
Nice to have
• We’d like to see a page with will make you dream, feel romantic and in love. To ensure the visitors that our boat is perfect for a dream holiday. Imagine being in a secluded white sand beach bay all alone with your loved ones, in a beautiful luxurious boat. Now stop dreaming and join us to make your dreams come true. Lastly, because of virus, we should also mention that we do proper cleaning of boat after every use (COVID free).

Velmōria is a Sanskrit word that means "wandering" or "world", with the connotation of cyclic, circuitous change. It is also the concept of rebirth and "cyclicality of all life, matter, existence", a fundamental belief of most Indian religions. In short, it is the cycle of death and rebirth.
Should not have
• It should not be only for one system, all devices should be able to see that page properly.

```html
<!DOCTYPE html>
<html lang="en">
<head>
<meta charset="utf-8">
<title>Velmoria — Sailing Boat</title>
<link rel="stylesheet" href="https://fonts.googleapis.com/css2?family=Poppins:wght@400;500;600;700;800;900&family=Tinos&display=swap">
<style>
:root{
  --navy:#0c2552;
  --navy-deep:#0a1f45;
  --blue:#1f63c9;
  --blue-bright:#2a74e0;
  --sand:#f3efee;
  --ink:#1b1b1b;
  --muted:#555b66;
  --white:#ffffff;
  --line:#9dbcec;
}
*{margin:0;padding:0;box-sizing:border-box}
html,body{width:1200px;height:5000px;overflow:hidden}
body{position:relative;font-family:"Poppins",sans-serif;color:var(--ink);background:var(--white)}
.abs{position:absolute}
.btn{position:absolute;background:var(--blue);color:var(--white);font-weight:700;font-size:10px;letter-spacing:.3px;border-radius:14px;display:flex;align-items:center;justify-content:center;text-transform:uppercase}
.section-title{position:absolute;left:0;width:1200px;text-align:center;font-weight:900;font-size:34px;letter-spacing:-.5px;color:var(--ink)}
.ghost{position:absolute;left:0;width:1200px;text-align:center;font-weight:900;font-size:50px;color:transparent;-webkit-text-stroke:1px #c9d8f2;letter-spacing:2px;opacity:.8}

/* Header & hero */
.hero{left:0;top:0;width:1200px;height:761px;background:linear-gradient(180deg,#6f8fa8 0%,#4b6a3f 14%,#3f5e33 40%,#6d7b5e 56%,#1c7c95 66%,#0f5f80 82%,#0a4564 100%)}
.logo{left:135px;top:66px;font-weight:800;font-size:25px;color:var(--white);letter-spacing:.5px}
.logo-dot{left:186px;top:26px;width:34px;height:34px;border-radius:50%;border:2px solid var(--white)}
.follow{left:540px;top:38px;font-size:9px;color:var(--white);font-weight:500}
.social{top:30px;width:26px;height:26px;border-radius:50%}
.call{left:740px;top:24px}
.call-label{left:788px;top:22px;font-size:12px;color:var(--white);font-weight:500}
.call-num{left:788px;top:40px;font-size:20px;color:#cde3ff;font-weight:500;letter-spacing:.5px}
.lang{left:959px;top:30px;width:106px;height:32px;background:var(--white);border:1px solid #ccc;font-size:9px;font-weight:600;display:flex;align-items:center;gap:6px;padding-left:10px}
.lang-flag{width:16px;height:10px;background:linear-gradient(#c8102e,#012169)}
.nav{left:431px;top:84px;display:flex;gap:25px;font-size:11px;font-weight:500;color:var(--white)}
.nav span{padding:3px 7px}
.nav .active{background:var(--navy)}
.hero-title{left:0;top:292px;width:1200px;text-align:center;font-size:92px;font-weight:900;color:var(--white);letter-spacing:-1px}

/* Boat */
.boat-band{left:0;top:761px;width:1200px;height:268px;background:var(--navy)}
.boat-ghost{top:800px;-webkit-text-stroke:1px #2b4a80;font-size:80px}
.boat-title{top:825px;color:var(--white)}
.toy-frame{left:82px;top:1174px;width:1036px;height:311px;border:2px solid var(--line);border-top:none;border-radius:0 0 8px 8px}
.toy-frame-inner{left:88px;top:1174px;width:1024px;height:305px;border:1px solid var(--line);border-top:none;border-radius:0 0 6px 6px}
.boat-card{top:928px;width:451px;height:415px;background:var(--white);box-shadow:0 4px 18px rgba(0,0,0,.15)}
.boat-card .photo{position:absolute;left:12px;top:15px;width:427px;height:231px;border-radius:6px}
.boat-card h3{position:absolute;left:32px;top:270px;font-size:18px;font-weight:800}
.boat-card p{position:absolute;left:32px;top:306px;width:380px;font-family:"Tinos",serif;font-size:13px;line-height:17px;color:#333}
.boat-card .btn{left:32px;top:359px;width:87px;height:27px}
.toy{top:1390px;width:170px;text-align:center}
.toy svg{display:block;margin:0 auto}
.toy span{display:inline-block;margin-top:10px;background:var(--white);padding:0 8px;font-size:12px;font-weight:600}

/* Welcome */
.welcome-bg{left:0;top:1559px;width:1200px;height:456px;background:var(--sand)}
.welcome-photo{left:0;top:1559px;width:596px;height:456px;border-radius:0 70px 70px 0;background:linear-gradient(160deg,#1577a8 0%,#0d5e8c 45%,#0a3f63 100%)}
.welcome-kicker{left:656px;top:1615px;font-size:17px;font-weight:500}
.welcome-name{left:656px;top:1640px;font-size:36px;font-weight:800;color:var(--navy)}
.welcome-rule{left:656px;top:1694px;width:48px;height:3px;background:var(--blue)}
.welcome-text{left:656px;top:1730px;width:412px;font-size:13.5px;line-height:22.4px;color:#333}
.welcome-btn{left:657px;top:1921px;width:105px;height:30px}

/* Events */
.events-ghost{top:2092px}
.events-title{top:2068px}
.event{top:2190px;width:298px;height:376px;background:var(--blue);border-radius:5px;overflow:hidden}
.event .photo{position:absolute;left:0;top:0;width:298px;height:235px}
.event .date{position:absolute;left:27px;top:194px;width:42px;height:56px;background:var(--blue);color:var(--white);text-align:center;border-radius:4px}
.event .date small{display:block;font-size:8px;font-weight:600;margin-top:9px}
.event .date b{display:block;font-size:20px;font-weight:500;line-height:22px}
.event h4{position:absolute;left:28px;top:252px;width:250px;font-size:13.5px;line-height:20px;font-weight:700;color:var(--white)}
.event p{position:absolute;left:28px;top:302px;width:220px;font-size:10.5px;line-height:13px;color:#dbe7fb}
.event .go{position:absolute;left:261px;top:338px;width:26px;height:26px;border-radius:50%;background:var(--white)}

/* Videos */
.videos-bg{left:0;top:2636px;width:1200px;height:547px;background:var(--sand)}
.videos-ghost{top:2676px}
.videos-title{top:2682px}
.video{top:2768px;width:456px;height:307px}
.video .play{position:absolute;left:50%;top:50%;width:48px;height:48px;margin:-24px 0 0 -24px;border-radius:50%;background:var(--white)}
.videos-btn{left:531px;top:3119px;width:138px;height:29px}

/* Reviews */
.reviews-ghost{top:3250px}
.reviews-title{top:3260px}
.review{top:3380px;width:245px;height:295px;background:var(--white);border-radius:8px;box-shadow:0 3px 16px rgba(0,0,0,.12)}
.review .q{position:absolute;font-family:"Tinos",serif;font-size:70px;font-weight:700;color:#d9d9d9;line-height:1}
.review .q.open{left:-2px;top:-16px}
.review .q.close{right:-2px;bottom:-44px}
.review p{position:absolute;left:39px;top:40px;width:172px;font-size:11px;line-height:17.3px;color:#333}
.review .avatar{position:absolute;left:39px;top:226px;width:42px;height:42px;border-radius:50%;background:linear-gradient(135deg,#8ea7c4,#5b6f86)}
.review .stars{position:absolute;left:96px;top:230px;font-size:11px;letter-spacing:1px;color:var(--blue)}
.review .name{position:absolute;left:96px;top:248px;font-size:11px;font-weight:600;color:var(--blue)}
.dots{left:560px;top:3728px;display:flex;gap:14px}
.dots i{display:block;width:10px;height:10px;border-radius:50%;border:1.5px solid var(--blue)}
.dots i.on{background:var(--blue)}

/* Gallery */
.gallery-bg{left:0;top:3808px;width:1200px;height:523px;background:var(--sand)}
.gallery-ghost{top:3858px}
.gallery-title{top:3862px}
.shot{top:3956px;width:282px;height:262px;border-radius:8px}

/* Subscribe */
.subscribe{left:0;top:4331px;width:1200px;height:312px;background:linear-gradient(120deg,#1a5fcf 0%,#2c74e2 50%,#1d5cc2 100%)}
.subscribe h2{position:absolute;left:134px;top:58px;font-size:34px;line-height:40px;font-weight:800;color:var(--white);text-transform:uppercase}
.sub-form{position:absolute;left:136px;top:200px;width:557px;height:56px;border:4px solid var(--white);display:flex}
.sub-field{flex:0 0 404px;display:flex;align-items:center;gap:10px;padding-left:16px;color:var(--white);font-size:14px;font-weight:600}
.sub-go{flex:1;background:var(--white);color:var(--blue);font-weight:800;font-size:18px;display:flex;align-items:center;justify-content:center}

/* Footer */
.footer{left:0;top:4643px;width:1200px;height:357px;background:var(--navy)}
.foot-logo{left:166px;top:132px;font-size:25px;font-weight:700;color:var(--white);letter-spacing:.5px}
.foot-dot{left:216px;top:92px;width:30px;height:30px;border:2px solid var(--white);border-radius:50%}
.foot-col h5{font-size:11px;font-weight:700;color:var(--white);margin-bottom:20px}
.foot-col a{display:block;font-size:11px;color:#d5def0;line-height:20px;text-decoration:none}
.contact-row{display:flex;gap:14px;align-items:flex-start;margin-bottom:22px;font-size:11px;line-height:14px;color:#d5def0}
.contact-row .ic{flex:0 0 22px;height:22px;border-radius:50%;background:var(--white)}
.copyright{left:0;top:4956px;width:1200px;text-align:center;font-size:9px;color:#c7d2ea}
</style>
</head>
<body>

<!-- Header & hero -->
<div class="abs hero" role="img" aria-label="Aerial view of a white sailing yacht anchored in a turquoise cove below green wooded hills"></div>
<div class="abs logo-dot"></div>
<div class="abs logo">VELMORIA</div>
<div class="abs follow">FOLLOW US</div>
<div class="abs social" style="left:616px;background:#3b5bb5"></div>
<div class="abs social" style="left:650px;background:#2ba3e8"></div>
<div class="abs social" style="left:684px;background:var(--navy)"></div>
<svg class="abs call" width="36" height="36" viewBox="0 0 36 36" fill="none" stroke="#fff" stroke-width="2"><path d="M8 6l6 0 3 8-4 3c2 4 5 7 9 9l3-4 8 3v6c0 2-2 3-4 3C17 33 3 19 3 10c0-2 1-4 3-4z"/></svg>
<div class="abs call-label">Call Us</div>
<div class="abs call-num">555.014.2290</div>
<div class="abs lang"><span class="lang-flag"></span>ENGLISH<svg width="8" height="6" viewBox="0 0 8 6" style="margin-left:12px"><path d="M0 0h8L4 5z" fill="#333"/></svg></div>
<div class="abs nav"><span class="active">HOME</span><span>ABOUT US</span><span>SERVICES</span><span>REVIEWS</span><span>VIDEOS</span><span>GALLERY</span><span>EVENTS</span><span>CONTACT US</span></div>
<h1 class="abs hero-title">SAILING BOAT</h1>

<!-- Boat -->
<div class="abs boat-band"></div>
<div class="ghost boat-ghost">BOAT</div>
<h2 class="section-title boat-title">BOAT</h2>
<div class="abs toy-frame"></div>
<div class="abs toy-frame-inner"></div>

<article class="abs boat-card" style="left:130px">
  <div class="photo" role="img" aria-label="Sunset over the sea seen from the deck of a sailing boat" style="background:linear-gradient(180deg,#6a7f96 0%,#c98d4a 45%,#e8a43b 58%,#3b2a1f 100%)"></div>
  <h3>TENDER BOAT</h3>
  <p>Lorem ipsum dolor sit amet, consectetur adipiscing elit, sed do eiusmod tempor incididunt ut labore</p>
  <div class="btn">Read more</div>
</article>
<article class="abs boat-card" style="left:611px">
  <div class="photo" role="img" aria-label="Yacht at anchor in clear turquoise water near a rocky shore" style="background:linear-gradient(180deg,#5f7850 0%,#8a8e7a 30%,#2c9bb5 55%,#137593 100%)"></div>
  <h3>PULL RINGOS</h3>
  <p>Lorem ipsum dolor sit amet, consectetur adipiscing elit, sed do eiusmod tempor incididunt ut labore</p>
  <div class="btn">Read more</div>
</article>

<div class="abs toy" style="left:90px">
  <svg width="50" height="50" viewBox="0 0 50 50" fill="none" stroke="#1f63c9" stroke-width="2"><rect x="6" y="20" width="26" height="16" rx="8"/><path d="M36 8v30c0 4-4 6-8 6M36 8h4"/></svg>
  <span>Snorkeling</span>
</div>
<div class="abs toy" style="left:245px">
  <svg width="50" height="50" viewBox="0 0 50 50" fill="none" stroke="#1f63c9" stroke-width="2"><path d="M10 8h12l-2 34h-8zM28 8h12l-2 34h-8zM12 16h8M30 16h8"/></svg>
  <span>Diving Equipment</span>
</div>
<div class="abs toy" style="left:472px">
  <svg width="50" height="50" viewBox="0 0 50 50" fill="none" stroke="#1f63c9" stroke-width="2"><path d="M10 10l30 30M40 10L10 40"/><ellipse cx="42" cy="42" rx="4" ry="7" transform="rotate(-45 42 42)" fill="#1f63c9"/><ellipse cx="8" cy="42" rx="4" ry="7" transform="rotate(45 8 42)" fill="#1f63c9"/></svg>
  <span>Paddle and Surfing boards</span>
</div>
<div class="abs toy" style="left:649px">
  <svg width="50" height="50" viewBox="0 0 50 50" fill="none" stroke="#1f63c9" stroke-width="2"><path d="M4 30c6-8 30-10 42-2-6 6-30 8-42 2z" fill="#1f63c9"/><circle cx="22" cy="16" r="4"/><path d="M4 40c6 3 10-3 16 0s10 3 16 0 8 3 12 0"/></svg>
  <span>Zumflo</span>
</div>
<div class="abs toy" style="left:791px">
  <svg width="50" height="50" viewBox="0 0 50 50" fill="none" stroke="#1f63c9" stroke-width="2"><path d="M4 10c6 3 10-3 16 0s10 3 16 0 8 3 12 0M4 16c6 3 10-3 16 0s10 3 16 0 8 3 12 0"/><path d="M8 32l18-4 12 4" stroke-width="4"/><circle cx="40" cy="30" r="4"/><path d="M4 44h42"/></svg>
  <span>Fintrak</span>
</div>
<div class="abs toy" style="left:932px">
  <svg width="50" height="50" viewBox="0 0 50 50" fill="none" stroke="#1f63c9" stroke-width="2"><path d="M14 6h8l3 6 3-6h8l4 10v28H10V16z"/><path d="M10 26h30M10 34h30"/></svg>
  <span>Life Jackets</span>
</div>

<!-- Welcome -->
<div class="abs welcome-bg"></div>
<div class="abs welcome-photo" role="img" aria-label="Scuba diver swimming underwater above a reef"></div>
<div class="abs welcome-kicker">Welcome to</div>
<h2 class="abs welcome-name">VELMORIA</h2>
<div class="abs welcome-rule"></div>
<p class="abs welcome-text">At vero eos et accusamus et iusto odio dignissimos ducimus qui blanditiis praesentium voluptatum deleniti atque corr upti quos dolores et quas molestias excepturi sint occaecati cupiditate non provident, similique sunt in culpa qui officia deserunt mollitia animi, id est laborum et dolorum fuga. Et harum quidem rerum facilis est et expedita distinctio. Nam libero tempore, cum soluta nobis.</p>
<div class="btn welcome-btn">Read more</div>

<!-- Latest events -->
<div class="ghost events-ghost">LATEST EVENTS</div>
<h2 class="section-title events-title">LATEST EVENTS</h2>

<article class="abs event" style="left:132px">
  <div class="photo" role="img" aria-label="Aerial view of a yacht over deep blue water and reef" style="background:linear-gradient(160deg,#1a6f92 0%,#12587c 50%,#0e4a6b 100%)"></div>
  <div class="date"><small>AUG</small><b>13</b></div>
  <h4>Sed ut perspiciatis unde omnis iste natus error</h4>
  <p>At vero eos et accusamus et iusto odio dignissimos ducimus qui blanditiis praese ntium voluptatum.</p>
  <svg class="go" viewBox="0 0 26 26"><path d="M11 8l5 5-5 5" fill="none" stroke="#1b1b1b" stroke-width="2"/></svg>
</article>
<article class="abs event" style="left:450px">
  <div class="photo" role="img" aria-label="Golden sunset beside a sailing boat hull" style="background:linear-gradient(180deg,#7d8a98 0%,#d39a4e 50%,#e9a23a 62%,#3a2a22 100%)"></div>
  <div class="date"><small>AUG</small><b>13</b></div>
  <h4>Sed ut perspiciatis unde omnis iste natus error</h4>
  <p>At vero eos et accusamus et iusto odio dignissimos ducimus qui blanditiis praese ntium voluptatum.</p>
  <svg class="go" viewBox="0 0 26 26"><path d="M11 8l5 5-5 5" fill="none" stroke="#1b1b1b" stroke-width="2"/></svg>
</article>
<article class="abs event" style="left:771px">
  <div class="photo" role="img" aria-label="Guests relaxing on a tender boat loaded with water toys" style="background:linear-gradient(160deg,#2a86b8 0%,#8a7a66 45%,#2c6e96 100%)"></div>
  <div class="date"><small>AUG</small><b>13</b></div>
  <h4>Sed ut perspiciatis unde omnis iste natus error</h4>
  <p>At vero eos et accusamus et iusto odio dignissimos ducimus qui blanditiis praese ntium voluptatum.</p>
  <svg class="go" viewBox="0 0 26 26"><path d="M11 8l5 5-5 5" fill="none" stroke="#1b1b1b" stroke-width="2"/></svg>
</article>

<!-- Videos -->
<div class="abs videos-bg"></div>
<div class="ghost videos-ghost">VIDEOS</div>
<h2 class="section-title videos-title">VIDEOS</h2>
<div class="abs video" style="left:132px" role="img" aria-label="Video still of a yacht in a bright turquoise bay under blue sky">
  <div style="position:absolute;inset:0;background:linear-gradient(180deg,#3f8fd6 0%,#7fc0ea 35%,#20b5c8 55%,#0c8cb0 100%)"></div>
  <svg class="play" viewBox="0 0 48 48"><path d="M19 14l16 10-16 10z" fill="#1f63c9"/></svg>
</div>
<div class="abs video" style="left:610px" role="img" aria-label="Video still of a sail against the setting sun over the sea">
  <div style="position:absolute;inset:0;background:linear-gradient(160deg,#3a3f4a 0%,#b7864c 40%,#e6a545 55%,#2a2d34 100%)"></div>
  <svg class="play" viewBox="0 0 48 48"><path d="M19 14l16 10-16 10z" fill="#1f63c9"/></svg>
</div>
<div class="btn videos-btn">View all videos</div>

<!-- Reviews -->
<div class="ghost reviews-ghost">CUSTOMER REVIEWS</div>
<h2 class="section-title reviews-title">CUSTOMER REVIEWS</h2>

<article class="abs review" style="left:64px"><span class="q open">&ldquo;</span><p>At vero eos et accusamus et iusto odio dignissimos ducim us qui blanditiis praesentium volup tatum deleniti atque corrupti quos dolores et quas molestias excep turi sint occaecati cupidi tate non provident, occur in which toil and pain can procure .</p><div class="avatar" role="img" aria-label="Reviewer portrait"></div><div class="stars">★★★★★</div><div class="name">DANIEL</div><span class="q close">&rdquo;</span></article>
<article class="abs review" style="left:344px"><span class="q open">&ldquo;</span><p>At vero eos et accusamus et iusto odio dignissimos ducim us qui blanditiis praesentium volup tatum deleniti atque corrupti quos dolores et quas molestias excep turi sint occaecati cupidi tate non provident, occur in which toil and pain can procure .</p><div class="avatar" role="img" aria-label="Reviewer portrait"></div><div class="stars">★★★★★</div><div class="name">DANIEL</div><span class="q close">&rdquo;</span></article>
<article class="abs review" style="left:625px"><span class="q open">&ldquo;</span><p>At vero eos et accusamus et iusto odio dignissimos ducim us qui blanditiis praesentium volup tatum deleniti atque corrupti quos dolores et quas molestias excep turi sint occaecati cupidi tate non provident, occur in which toil and pain can procure .</p><div class="avatar" role="img" aria-label="Reviewer portrait"></div><div class="stars">★★★★★</div><div class="name">DANIEL</div><span class="q close">&rdquo;</span></article>
<article class="abs review" style="left:907px"><span class="q open">&ldquo;</span><p>At vero eos et accusamus et iusto odio dignissimos ducim us qui blanditiis praesentium volup tatum deleniti atque corrupti quos dolores et quas molestias excep turi sint occaecati cupidi tate non provident, occur in which toil and pain can procure .</p><div class="avatar" role="img" aria-label="Reviewer portrait"></div><div class="stars">★★★★★</div><div class="name">DANIEL</div><span class="q close">&rdquo;</span></article>
<div class="abs dots"><i></i><i></i><i class="on"></i><i></i><i></i></div>

<!-- Gallery -->
<div class="abs gallery-bg"></div>
<div class="ghost gallery-ghost">GALLERY</div>
<h2 class="section-title gallery-title">GALLERY</h2>
<div class="abs shot" style="left:16px;background:linear-gradient(160deg,#2a86b8,#8a7a66 50%,#2c6e96)" role="img" aria-label="Tender boat with guests and water toys"></div>
<div class="abs shot" style="left:311px;background:linear-gradient(160deg,#5f6b4a,#2a8aa8 55%,#0f5e80)" role="img" aria-label="Aerial view of a yacht off a rocky green coastline"></div>
<div class="abs shot" style="left:606px;background:linear-gradient(180deg,#7d8a98,#d39a4e 50%,#e9a23a 62%,#3a2a22)" role="img" aria-label="Sunset seen past the mast and rigging"></div>
<div class="abs shot" style="left:901px;background:linear-gradient(180deg,#6e7a88,#c9944f 45%,#2d2a28)" role="img" aria-label="Cockpit and steering wheel at sunset"></div>
<svg class="abs" style="left:566px;top:4262px" width="16" height="26" viewBox="0 0 16 26" fill="none" stroke="#333" stroke-width="2"><path d="M13 2L3 13l10 11"/></svg>
<svg class="abs" style="left:614px;top:4262px" width="16" height="26" viewBox="0 0 16 26" fill="none" stroke="#333" stroke-width="2"><path d="M3 2l10 11L3 24"/></svg>

<!-- Subscribe -->
<section class="abs subscribe">
  <h2>Monthly fee<br>for maintenance<br>and updates</h2>
  <div class="sub-form">
    <div class="sub-field"><svg width="14" height="10" viewBox="0 0 14 10"><rect width="14" height="10" fill="#fff"/><path d="M0 0l7 6 7-6" fill="none" stroke="#1f63c9"/></svg>E MAIL ID</div>
    <div class="sub-go">SUBSCRIBE</div>
  </div>
</section>

<!-- Footer -->
<footer class="abs footer">
  <div class="abs foot-dot"></div>
  <div class="abs foot-logo">VELMORIA</div>
  <div class="abs foot-col" style="left:449px;top:56px">
    <h5>MENU</h5>
    <a>HOME</a><a>ABOUT US</a><a>SERVICES</a><a>REVIEWS</a><a>VIDEOS</a><a>GALLERY</a><a>EVENTS</a><a>CONTACT US</a>
  </div>
  <div class="abs foot-col" style="left:648px;top:56px">
    <h5>CONTACT US</h5>
    <div class="contact-row"><span class="ic"></span><div>Call Us<br>555.014.2290</div></div>
    <div class="contact-row"><span class="ic"></span><div>E mail Us<br>info@velmoria.com</div></div>
  </div>
  <div class="abs foot-col" style="left:963px;top:56px">
    <h5>FOLLOW US</h5>
    <div class="contact-row"><span class="ic"></span><div>Like us on<br>FRIENDLINE</div></div>
    <div class="contact-row"><span class="ic"></span><div>Follow us on<br>CHIRPER</div></div>
    <div class="contact-row"><span class="ic"></span><div>Follow us on<br>WORKLINK</div></div>
  </div>
</footer>
<div class="abs copyright">Copyright © 2020 All Rights Reserved</div>

</body>
</html>
```